Medical Skincare services/menu/pricing Booklet 12 pages

We need produce a 12-page glossy, saddle-stitched booklet (5 1/2" tall X 81/2" wide). The booklet will be used as a services menu for a skin care salon. I have mocked up the booklet (w/ all copy) in WORD and I've provided a separate PDF of the accurate page order (see files attached). IMPORTANT: Feel free to use your creativity yet style-wise it should kinda match my wife's website colors and text style. Her clients are demanding so she wants a clean, high end, modern look (ala Pebble maybe?). See her website for a frame of reference www.GlowWithMarta.com

Target Market(s)

upscale female, professional women, teens with acne

Industry/Entity Type

Medical

Requirements
Must have
• the pics in the mock up are important. I've attached them here

```html
<!DOCTYPE html>
<html lang="en">
<head>
<meta charset="utf-8">
<title>Glow With Marta – Back Cover</title>
<link href="https://fonts.googleapis.com/css2?family=Montserrat:wght@300;400;500&display=swap" rel="stylesheet">
<style>
  :root {
    --slate: #5d5a67;
    --taupe: #a89677;
    --cream: #f4f1ea;
    --photo-light: #b59a86;
    --photo-mid: #7a5a46;
    --photo-dark: #4a4a4e;
  }
  * { margin: 0; padding: 0; box-sizing: border-box; }
  html, body { width: 1200px; height: 846px; overflow: hidden; }
  body {
    background: var(--slate);
    font-family: 'Montserrat', sans-serif;
    color: var(--cream);
  }
  .cover { position: relative; width: 1200px; height: 846px; }

  .portrait {
    position: absolute; left: 243px; top: 158px; width: 284px; height: 487px;
    background: linear-gradient(180deg, var(--photo-light) 0%, var(--photo-mid) 40%, var(--photo-dark) 100%);
  }
  .owner { position: absolute; right: 673px; text-align: right; color: var(--taupe); }
  .owner-name { top: 660px; font-size: 29px; font-weight: 500; letter-spacing: 0.3px; }
  .owner-title { top: 698px; font-size: 15px; font-weight: 400; }

  .spine { position: absolute; left: 548px; top: 158px; width: 2px; height: 688px; background: var(--taupe); }

  .info-band {
    position: absolute; left: 549px; top: 402px; width: 596px; height: 238px;
    background: var(--taupe);
    overflow: hidden;
  }
  .band-divider { position: absolute; left: 284px; top: 17px; width: 2px; height: 215px; background: var(--cream); }

  .booking { position: absolute; right: 343px; top: 18px; width: 240px; text-align: right; }
  .booking-label { font-size: 18px; font-weight: 300; letter-spacing: 0.3px; }
  .booking-url { font-size: 17px; font-weight: 500; letter-spacing: -0.1px; margin-top: 6px; white-space: nowrap; }
  .booking-call { font-size: 18px; font-weight: 300; margin-top: 28px; }
  .booking-phone { font-size: 22px; font-weight: 500; margin-top: 3px; }

  .hours { position: absolute; left: 312px; top: 18px; }
  .hours-title { font-size: 18px; font-weight: 300; letter-spacing: 0.3px; margin-bottom: 10px; }
  .hours-table { border-collapse: collapse; font-size: 16px; font-weight: 400; }
  .hours-table td { height: 26.4px; padding: 0; vertical-align: middle; white-space: nowrap; }
  .hours-table .day { width: 101px; }
  .hours-table small { font-size: 12px; font-weight: 300; }

  .brand { position: absolute; left: 570px; top: 653px; font-size: 29px; font-weight: 300; color: var(--taupe); letter-spacing: 1.5px; }
  .address { position: absolute; left: 570px; top: 697px; font-size: 19px; font-weight: 400; font-style: normal; color: var(--taupe); line-height: 24px; letter-spacing: 0.3px; }
</style>
</head>
<body>
<main class="cover">
  <div class="portrait" role="img" aria-label="Portrait photo of the medical aesthetician in a grey fur wrap"></div>
  <p class="owner owner-name">Marta Lindqvist</p>
  <p class="owner owner-title">Medical Aesthetician &amp; Owner</p>

  <div class="spine"></div>

  <section class="info-band">
    <div class="booking">
      <p class="booking-label">BOOK ONLINE</p>
      <p class="booking-url">www.GlowWithMarta.com</p>
      <p class="booking-call">Or Call/Text</p>
      <p class="booking-phone">(720) 555-0148</p>
    </div>
    <div class="band-divider"></div>
    <div class="hours">
      <p class="hours-title">BY APPT. HOURS:</p>
      <table class="hours-table">
        <tr><td class="day">Monday</td><td>10:00<small>am</small> - 4:00<small>pm</small></td></tr>
        <tr><td class="day">Tuesday</td><td>10:00<small>am</small> - 6:00<small>pm</small></td></tr>
        <tr><td class="day">Wednesday</td><td>10:00<small>am</small> - 6:00<small>pm</small></td></tr>
        <tr><td class="day">Thursday</td><td>10:00<small>am</small> - 6:00<small>pm</small></td></tr>
        <tr><td class="day">Friday</td><td>10:00<small>am</small> - 6:00<small>pm</small></td></tr>
        <tr><td class="day">Saturday</td><td>10:00<small>am</small> - 4:00<small>pm</small></td></tr>
        <tr><td class="day">Sunday</td><td>Closed</td></tr>
      </table>
    </div>
  </section>

  <p class="brand">GLOW WITH MARTA</p>
  <address class="address">4127 Aspen Ridge Ave #200<br>Cedar Hollow, Colorado 80199</address>
</main>
</body>
</html>
```